Pale Lanterns Old Lane Walk Poster Design

We need an A4 sized poster to promote our weekly true crime tours. This poster will be posted onto community noticeboards.
Lots of information and images can be viewed at the following links:-
www.palelanterns.com.au
www.palelanterns.com.au/bookings/
https://www.facebook.com/palelanternsoldlane/
https://www.examplereviews.com.au/Attraction_Review-g000000-d00000000-Reviews-Pale_Lanterns-Newcastle_Greater_Newcastle_New_South_Wales.html
There are also a number of images for possible use at the following link - we are open to intepretation:-
http://palelanterns.com.au/tour-photographs/
The font on our website is "SpecialElite" so we would like to continue using that font type.
Target Market(s)
Adults 25-65.
Font styles to use
Other font styles liked:
- Special Elite
Colors
Designer to choose colors to be used in the design.
Look and feel
Each slider illustrates characteristics of the customer's brand and the style your logo design should communicate.

```html
<!DOCTYPE html>
<html lang="en">
<head>
<meta charset="utf-8">
<title>Pale Lanterns Old Lane Walk Poster</title>
<link rel="stylesheet" href="https://fonts.googleapis.com/css2?family=Special+Elite&display=swap">
<style>
  :root {
    --backdrop: #2a2725;
    --slate: #3b3f44;
    --slate-dark: #2f3338;
    --band-red: #6e0606;
    --band-red-deep: #4a0303;
    --ink: #141414;
    --ink-soft: #1f1f1f;
    --quote: #c9c9c9;
    --quote-soft: #b0b0b0;
    --star: #f3ea1e;
    --alert-red: #e41313;
    --book-red: #8c1010;
    --title-ink: #15181b;
  }
  * { margin: 0; padding: 0; box-sizing: border-box; }
  html, body { width: 1000px; height: 1200px; overflow: hidden; }
  body {
    background: var(--backdrop);
    font-family: "Special Elite", "Courier New", monospace;
    position: relative;
  }
  .poster {
    position: absolute;
    left: 128px; top: 82px;
    width: 740px; height: 1045px;
    overflow: hidden;
    box-shadow: 0 6px 18px rgba(0,0,0,.55);
  }
  .column { position: absolute; top: 0; height: 100%; }
  .column--left { left: 0; width: 242px; background: linear-gradient(180deg, var(--slate) 0%, var(--slate-dark) 100%); }
  .column--centre { left: 242px; width: 250px; background: linear-gradient(180deg, var(--band-red) 0%, var(--band-red-deep) 100%); }
  .column--right { left: 492px; width: 248px; background: linear-gradient(180deg, var(--slate) 0%, var(--slate-dark) 100%); }
  .street-scene {
    position: absolute; left: 242px; top: 110px; width: 250px; height: 430px;
    background: linear-gradient(180deg, rgba(120,20,20,.0) 0%, rgba(150,40,40,.55) 35%, rgba(90,10,10,.6) 75%, rgba(74,3,3,0) 100%);
  }
  .brand-mark {
    position: absolute; left: 242px; top: 38px; width: 250px;
    text-align: center; font-size: 24px; color: var(--ink); letter-spacing: 2px;
  }
  .review { position: absolute; top: 112px; width: 220px; color: var(--quote); font-size: 17px; line-height: 19px; }
  .review--left { left: 10px; text-align: right; }
  .review--right { left: 508px; text-align: left; }
  .review .stars { color: var(--star); font-size: 27px; letter-spacing: 1px; line-height: 28px; margin-bottom: 4px; }
  .review .source { font-size: 14px; color: var(--quote-soft); }
  .title { position: absolute; left: 0; width: 740px; text-align: center; color: var(--title-ink); line-height: 1; }
  .title--top { top: 236px; font-size: 228px; letter-spacing: 6px; }
  .title--bottom { top: 455px; font-size: 112px; letter-spacing: 6px; }
  .tagline { position: absolute; font-size: 27px; color: var(--ink); white-space: nowrap; letter-spacing: 1px; }
  .tagline .on-band { color: var(--alert-red); opacity: .8; }
  .tagline--one { left: 100px; top: 590px; }
  .tagline--two { left: 372px; top: 628px; }
  .tagline--three { left: 60px; top: 664px; font-size: 21px; color: var(--ink-soft); }
  .tour-label { position: absolute; color: var(--alert-red); font-size: 22px; line-height: 29px; letter-spacing: 1px; }
  .tour-label--left { right: 504px; top: 748px; text-align: right; }
  .tour-label--right { left: 500px; top: 776px; }
  .pointer { position: absolute; background: rgba(20,20,20,.25); border-radius: 10px; }
  .pointer--top { left: 254px; top: 752px; width: 120px; height: 34px; }
  .pointer--bottom { left: 372px; top: 812px; width: 110px; height: 30px; }
  .book-call { position: absolute; left: 242px; top: 782px; width: 250px; text-align: center; font-size: 42px; color: var(--book-red); letter-spacing: 1px; }
  .contact { position: absolute; top: 905px; text-align: center; color: var(--ink); font-size: 17px; line-height: 20px; }
  .contact svg { display: block; margin: 0 auto 18px; }
  .contact--phone { left: 0; width: 242px; }
  .contact--phone p { margin-top: 14px; }
  .contact--email { left: 242px; width: 250px; top: 900px; }
  .contact--web { left: 492px; width: 248px; top: 900px; }
  .contact--web p { margin-top: 6px; }
</style>
</head>
<body>
  <main class="poster">
    <div class="column column--left"></div>
    <div class="column column--centre"></div>
    <div class="column column--right"></div>
    <div class="street-scene" role="img" aria-label="Red-tinted photograph of an old lane street scene at dusk"></div>

    <div class="brand-mark">Pale Lanterns</div>

    <section class="review review--left">
      <div class="stars">★★★★★</div>
      <p>Fabulous addition<br>to New Castle</p>
      <p class="source">-from LocalReviews</p>
    </section>
    <section class="review review--right">
      <div class="stars">★★★★★</div>
      <p>History comes<br>arrive</p>
      <p class="source">-Joan P</p>
    </section>

    <h1 class="title title--top">PALE</h1>
    <h2 class="title title--bottom">LANTERNS</h2>

    <p class="tagline tagline--one">..revisi<span class="on-band">t the scenes</span></p>
    <p class="tagline tagline--two"><span class="on-band">of the</span> crimes..</p>
    <p class="tagline tagline--three">take a walk on the dark side</p>

    <p class="tour-label tour-label--left">TRUE CRIME<br>TOUR</p>
    <div class="pointer pointer--top" role="img" aria-label="Drawn pointing hand"></div>
    <p class="book-call">BOOK</p>
    <div class="pointer pointer--bottom" role="img" aria-label="Drawn pointing hand"></div>
    <p class="tour-label tour-label--right">CONFESSIONS<br>OF A<br>SERIAL KILLER</p>

    <div class="contact contact--phone">
      <svg width="36" height="40" viewBox="0 0 24 24" aria-hidden="true"><path fill="#141414" d="M6.6 10.8c1.4 2.8 3.8 5.1 6.6 6.6l2.2-2.2c.3-.3.7-.4 1-.2 1.1.4 2.3.6 3.6.6.6 0 1 .4 1 1V20c0 .6-.4 1-1 1C10.6 21 3 13.4 3 4c0-.6.4-1 1-1h3.5c.6 0 1 .4 1 1 0 1.3.2 2.5.6 3.6.1.3 0 .7-.2 1z"/></svg>
      <p>0491 570 156</p>
    </div>
    <div class="contact contact--email">
      <svg width="46" height="34" viewBox="0 0 46 34" aria-hidden="true"><rect x="1" y="1" width="44" height="32" fill="#141414"/><path d="M2 3 L23 19 L44 3" stroke="#4a0303" stroke-width="2" fill="none"/></svg>
      <p>info<br>@palelanterns<br>.com.au</p>
    </div>
    <div class="contact contact--web">
      <svg width="36" height="36" viewBox="0 0 36 36" aria-hidden="true"><g fill="none" stroke="#141414" stroke-width="2.4"><circle cx="18" cy="18" r="16"/><ellipse cx="18" cy="18" rx="7" ry="16"/><line x1="18" y1="2" x2="18" y2="34"/><line x1="2" y1="18" x2="34" y2="18"/><path d="M5 9 H31 M5 27 H31"/></g></svg>
      <p>www<br>.palelanterns<br>.com.au</p>
    </div>
  </main>
</body>
</html>
```